Looking for a modern elegant home improvment website

Looking for a new Design on current website . Please us www.brambleforkbuilders.com PIctures of recent work and stock photos that were attached , Free estimates , Explaining what we do , Similiar to www. brambleforkbuilders.com which is our current webpage . Colors can be different . I have attached our buisness card as well as our postcard we send out to homes . I would like a modern web page that our costumers can feel is professional so they can have a feeling of trust when they hire us . Our address should be on there . Licenesed & Insured should be somewhere on the page . Our Company Logo should be there as well . It would be nice to have a very modern website with great pictures of home interiors and exteriors . a page describing what we do is very important . facebook link to our page is a must as well as a instagram .
Updates

Reason: Looking for a elegant modern 5 page website with proper spelling and professional looking . I extended the deadline and upgraded .

Reason: Looking for more design options .

Target Market(s)

Home owners , Commerical buisness,

Industry/Entity Type

Home Improvement

Number of Pages Required

5+ page

Font styles to use
Serif

Requirements
Must have
• PIctures of recent work and stock photos that were attached , Free estimates , Explaining what we do , Similiar to www. brambleforkbuilders.com which is our current webpage . Colors can be different . I have attached our buisness card as well as our postcard we send out to homes . I would like a modern web page that our costumers can feel is professional so they can have a feeling of trust when they hire us . Our address should be on there . Licenesed & Insured should be somewhere on the page . Our Company Logo should be there as well .
Nice to have
• It would be nice to have a very modern website with great pictures of home interiors and exteriors . a page describing what we do is very important . facebook link to our page is a must as well as a instagram .

```html
<!DOCTYPE html>
<html lang="en">
<head>
<meta charset="utf-8">
<title>Bramble Fork Builders LLC</title>
<link href="https://fonts.googleapis.com/css2?family=Montserrat:wght@400;500;600;700&family=Open+Sans:wght@400;600&display=swap" rel="stylesheet">
<style>
:root{
  --navy:#2d4b74;
  --navy-dark:#1d3356;
  --navy-deep:#172a47;
  --ink:#2a3344;
  --muted:#6b7280;
  --line:#d6dbe3;
  --paper:#ffffff;
  --mist:#e8eaee;
  --wood:#9a5a2a;
}
*{box-sizing:border-box;margin:0;padding:0}
html,body{width:1200px;height:3272px;overflow:hidden;background:var(--paper)}
body{font-family:"Open Sans",sans-serif;color:var(--ink);position:relative}
h1,h2,h3,h4{font-family:"Montserrat",sans-serif}
.section{position:absolute;left:0;width:1200px}

/* header */
.site-header{top:0;height:72px;display:flex;align-items:center;padding:0 152px;background:var(--paper)}
.brand{display:flex;align-items:center;gap:10px;font-family:"Montserrat",sans-serif;font-weight:600;font-size:15px;color:var(--navy)}
.brand-mark{width:22px;height:22px;background:var(--navy)}
.main-nav{margin-left:auto;display:flex;align-items:stretch;height:72px}
.main-nav a{display:flex;align-items:center;padding:0 18px;font-family:"Montserrat",sans-serif;font-size:13px;color:var(--ink);text-decoration:none}
.main-nav a.active{background:var(--navy);color:#fff}
.btn-estimate{align-self:center;margin-left:24px;background:var(--navy);color:#fff;font-family:"Montserrat",sans-serif;font-size:13px;padding:10px 26px;border-radius:3px}

/* hero */
.hero{top:72px;height:368px;background:linear-gradient(180deg,#c9ccd0 0%,#a8a49c 55%,#7c6f61 100%);text-align:center;color:#fff}
.hero-text{position:absolute;top:108px;left:0;width:100%}
.hero h1{font-size:36px;font-weight:600;text-shadow:0 1px 4px rgba(0,0,0,.35)}
.hero p{margin-top:8px;font-family:"Montserrat",sans-serif;font-size:21px;text-shadow:0 1px 4px rgba(0,0,0,.35)}
.btn-outline-light{display:inline-block;margin-top:28px;padding:9px 26px;background:var(--navy);color:#fff;font-size:13px;font-family:"Montserrat",sans-serif;border-radius:3px}
.hero-arrow{position:absolute;top:168px;width:28px;height:28px;border-radius:50%;background:rgba(255,255,255,.35)}
.hero-arrow.prev{left:96px}.hero-arrow.next{right:96px}

/* section titles */
.section-title{text-align:center;font-size:36px;font-weight:600;color:var(--navy)}
.section-sub{text-align:center;font-family:"Montserrat",sans-serif;font-size:17px;color:var(--ink);margin-top:4px}

/* services */
.services{top:490px;height:500px}
.pager{position:absolute;right:152px;top:24px;display:flex;gap:8px}
.pager span{width:22px;height:22px;border:1px solid var(--line);border-radius:3px}
.pager span.on{background:var(--navy);border-color:var(--navy)}
.service-cards{position:absolute;top:102px;left:152px;display:flex;gap:42px}
.service-card{width:280px}
.service-photo{height:200px}
.service-card h3{margin-top:20px;font-size:20px;font-weight:600;color:var(--navy)}
.service-card p{margin-top:8px;font-size:12.5px;line-height:1.55;color:var(--muted)}
.btn-small{display:inline-block;margin-top:18px;padding:6px 16px;border:1px solid var(--line);border-radius:14px;font-size:11px;color:var(--ink);font-family:"Montserrat",sans-serif}
.btn-small.filled{background:var(--navy);border-color:var(--navy);color:#fff}

/* about */
.about{top:1012px;height:392px;display:flex}
.about-copy{width:600px;background:var(--navy);color:#fff;padding:54px 60px 0 152px}
.about-copy h2{font-size:34px;font-weight:600}
.about-copy h4{font-size:15px;font-weight:500;margin-top:4px}
.about-copy p{margin-top:22px;font-size:12.5px;line-height:1.6;color:#dfe6f0}
.btn-outline{display:inline-block;margin-top:22px;padding:6px 18px;border:1px solid #fff;border-radius:14px;font-size:11px;font-family:"Montserrat",sans-serif}
.about-photo{width:600px;background:linear-gradient(135deg,#c98a4d,#8a4f22 60%,#5e3518)}

/* latest work */
.work{top:1456px;height:620px}
.work-grid{position:absolute;top:92px;left:152px;width:896px;height:440px}
.tile{position:absolute}
.tile.overlay{background:#34404f;color:#fff;display:flex;flex-direction:column;align-items:center;justify-content:center;gap:14px;font-family:"Montserrat",sans-serif;font-size:14px}
.tile.overlay .zoom{width:34px;height:34px;border-radius:50%;background:#fff;display:flex;align-items:center;justify-content:center}
.work .btn-small{position:absolute;top:548px;left:538px}

/* CTA */
.cta{top:2112px;height:200px;background:var(--navy-dark);color:#fff;text-align:center;padding-top:42px}
.cta h3{font-size:20px;font-weight:600}
.cta p{font-family:"Montserrat",sans-serif;font-size:16px;margin-top:4px}
.cta .btn-small{border-color:#fff;color:#fff;margin-top:20px}

/* testimonials */
.testimonials{top:2346px;height:370px}
.avatars{position:absolute;top:108px;left:0;width:100%;display:flex;justify-content:center;align-items:center;gap:34px}
.avatar{border-radius:50%;background:linear-gradient(160deg,#b7a48d,#6d7a8a)}
.avatar.side{width:58px;height:58px;opacity:.85}
.avatar.main{width:72px;height:72px;border:3px solid #fff;box-shadow:0 0 0 1px var(--line)}
.reviewer{position:absolute;top:196px;width:100%;text-align:center}
.reviewer h4{font-size:16px;font-weight:600;color:var(--navy)}
.reviewer span{font-size:12px;color:var(--muted)}
.quote{position:absolute;top:254px;left:400px;width:400px;text-align:center;font-size:12.5px;line-height:1.6;color:var(--muted)}
.quote-mark{position:absolute;top:232px;font-family:Georgia,serif;font-size:60px;color:#d4d8df;line-height:1}

/* contact */
.contact{top:2720px;height:400px;background:var(--mist)}
.contact .section-title{margin-top:36px}
.contact-form{position:absolute;top:132px;left:318px;width:270px}
.field{height:28px;background:#fff;border:1px solid var(--line);margin-bottom:10px;font-size:11px;color:#9aa1ad;padding:6px 10px}
.field.message{height:62px}
.btn-send{display:inline-flex;align-items:center;gap:6px;background:var(--navy);color:#fff;font-size:11px;padding:6px 16px;border-radius:14px;font-family:"Montserrat",sans-serif}
.contact-info{position:absolute;top:126px;left:606px;width:300px}
.info-row{display:flex;gap:12px;margin-bottom:20px;font-size:11.5px;line-height:1.5;color:var(--muted)}
.info-row b{display:block;color:var(--ink);font-weight:600}
.info-row svg{flex:none;margin-top:2px}

/* footer */
.site-footer{top:3120px;height:152px;background:var(--navy-deep);color:#c6d0de;text-align:center}
.socials{display:flex;justify-content:center;gap:10px;margin-top:-14px}
.socials span{width:28px;height:28px;border-radius:50%;background:#fff;border:2px solid var(--navy-deep)}
.footer-nav{margin-top:30px;display:flex;justify-content:center;gap:36px;font-family:"Montserrat",sans-serif;font-size:13px;color:#fff}
.footer-rule{width:520px;height:1px;background:#34496b;margin:16px auto 0}
.copyright{margin-top:12px;font-size:11px}
</style>
</head>
<body>

<header class="section site-header">
  <div class="brand"><span class="brand-mark"></span>Bramble Fork Builders LLC</div>
  <nav class="main-nav">
    <a class="active" href="#">Home</a>
    <a href="#">About Us</a>
    <a href="#">Services</a>
    <a href="#">Gallery</a>
    <a href="#">Contact Us</a>
  </nav>
  <span class="btn-estimate">Free Estimate</span>
</header>

<section class="section hero" role="img" aria-label="Bright finished living room interior with light walls and wood floors">
  <span class="hero-arrow prev"></span><span class="hero-arrow next"></span>
  <div class="hero-text">
    <h1>We are tile &amp; marble specialist</h1>
    <p>We build bathrooms , Kitchens , Additions and much more</p>
    <span class="btn-outline-light">Explore More</span>
  </div>
</section>

<section class="section services">
  <h2 class="section-title">Who We Are?</h2>
  <p class="section-sub">Get yourself the best General Contractor in the business!</p>
  <div class="pager"><span></span><span class="on"></span></div>
  <div class="service-cards">
    <article class="service-card">
      <div class="service-photo" role="img" aria-label="Newly installed hardwood floor in an empty room" style="background:linear-gradient(160deg,#d8d2c8,#8d6a48)"></div>
      <h3>Flooring</h3>
      <p>We install durable floors in hardwood, tile and stone, fitted with care and finished to last for years to come.</p>
      <span class="btn-small">Read More</span>
    </article>
    <article class="service-card">
      <div class="service-photo" role="img" aria-label="Tall new windows and doors in a bright room" style="background:linear-gradient(160deg,#efe9df,#b3875a)"></div>
      <h3>Windows and Doors</h3>
      <p>We replace windows and doors that seal out drafts, cut energy costs and add lasting curb appeal to any home.</p>
      <span class="btn-small filled">Read More</span>
    </article>
    <article class="service-card">
      <div class="service-photo" role="img" aria-label="Remodeled kitchen with wood cabinets and stone counters" style="background:linear-gradient(160deg,#d79a52,#7a4218)"></div>
      <h3>Kitchens and Bathrooms</h3>
      <p>We design and build kitchens and bathrooms with quality cabinets, tile and marble that suit the way you live.</p>
      <span class="btn-small">Read More</span>
    </article>
  </div>
</section>

<section class="section about">
  <div class="about-copy">
    <h2>About Us</h2>
    <h4>Licensed &amp; Fully Insured</h4>
    <p>Your home is the most important asset you have, so when you're ready to build or remodel, get yourself the best General Contractor in the business! We have been building for over 20 years, specializing in residential and commercial work. We are tile &amp; marble specialists. We build bathrooms, kitchens, additions and much more. Give us a call, we do great work and we are passionate about what we do. We are a family owned business.</p>
    <span class="btn-outline">Discover More</span>
  </div>
  <div class="about-photo" role="img" aria-label="Spacious kitchen with warm wood cabinets and an island"></div>
</section>

<section class="section work">
  <h2 class="section-title">Our Latest Work</h2>
  <p class="section-sub">Check out a few of our completed projects !</p>
  <div class="work-grid">
    <div class="tile" role="img" aria-label="Exterior porch with white railings and stairs" style="left:0;top:0;width:428px;height:220px;background:linear-gradient(160deg,#cfd3cf,#7f7a6e)"></div>
    <div class="tile" role="img" aria-label="Framed addition under construction" style="left:456px;top:0;width:204px;height:220px;background:linear-gradient(160deg,#d9c4a3,#8e6a45)"></div>
    <div class="tile" role="img" aria-label="Kitchen with dark granite counters" style="left:688px;top:0;width:208px;height:220px;background:linear-gradient(160deg,#b9875a,#3d2c22)"></div>
    <div class="tile" role="img" aria-label="Kitchen with wood cabinetry" style="left:0;top:240px;width:208px;height:200px;background:linear-gradient(160deg,#c57d3e,#6b3a19)"></div>
    <div class="tile" role="img" aria-label="Open kitchen and dining area" style="left:232px;top:240px;width:196px;height:200px;background:linear-gradient(160deg,#d4955a,#7b4722)"></div>
    <div class="tile overlay" style="left:456px;top:240px;width:440px;height:200px">
      <span>Restaurants</span>
      <span class="zoom"><svg width="14" height="14" viewBox="0 0 14 14"><circle cx="6" cy="6" r="4" fill="none" stroke="#2d4b74" stroke-width="1.6"/><line x1="9" y1="9" x2="13" y2="13" stroke="#2d4b74" stroke-width="1.6"/></svg></span>
    </div>
  </div>
  <span class="btn-small">View all Projects</span>
</section>

<section class="section cta">
  <h3>Our Team of Experts will make your Dreams into creative construction</h3>
  <p>Lets start making plans to build your dreams!</p>
  <span class="btn-small">Contact Us</span>
</section>

<section class="section testimonials">
  <h2 class="section-title">Testimonials</h2>
  <p class="section-sub">We always listen on our clients</p>
  <div class="avatars">
    <div class="avatar side" role="img" aria-label="Client portrait"></div>
    <div class="avatar main" role="img" aria-label="Client portrait"></div>
    <div class="avatar side" role="img" aria-label="Client portrait"></div>
  </div>
  <div class="reviewer"><h4>Dana Whitfield</h4><span>Millbrook, NY</span></div>
  <span class="quote-mark" style="left:362px">&ldquo;</span>
  <p class="quote">Great work, reliable, very professional about what they do. Thanks for a job well done.</p>
  <span class="quote-mark" style="left:812px">&rdquo;</span>
</section>

<section class="section contact">
  <h2 class="section-title">Contact Us</h2>
  <p class="section-sub">All fields are required.</p>
  <form class="contact-form">
    <div class="field">Name</div>
    <div class="field">Email</div>
    <div class="field">Subject</div>
    <div class="field message">Message</div>
    <span class="btn-send"><svg width="10" height="10" viewBox="0 0 10 10"><path d="M0 5 L10 0 L7 10 L5 6 Z" fill="#fff"/></svg>Send</span>
  </form>
  <div class="contact-info">
    <div class="info-row">
      <svg width="14" height="16" viewBox="0 0 14 16"><path d="M7 0a6 6 0 0 0-6 6c0 4.5 6 10 6 10s6-5.5 6-10a6 6 0 0 0-6-6z" fill="#2d4b74"/><circle cx="7" cy="6" r="2.2" fill="#e8eaee"/></svg>
      <div><b>Bramble Fork Builders LLC</b>48 Orchard Lane<br>Millbrook, NY 12545</div>
    </div>
    <div class="info-row">
      <svg width="14" height="12" viewBox="0 0 14 12"><rect width="14" height="12" rx="1" fill="#2d4b74"/><path d="M1 1l6 5 6-5" fill="none" stroke="#e8eaee" stroke-width="1.2"/></svg>
      <div><b>Email</b>hello@brambleforkbuilders.com</div>
    </div>
    <div class="info-row">
      <svg width="14" height="14" viewBox="0 0 14 14"><path d="M3 0l3 3-2 2c1 2 3 4 5 5l2-2 3 3-2 3C6 14 0 8 0 3z" fill="#2d4b74"/></svg>
      <div><b>Phone</b>(555) 014-2290</div>
    </div>
    <div class="info-row">
      <svg width="14" height="14" viewBox="0 0 14 14"><rect x="1" y="2" width="12" height="10" rx="1" fill="#2d4b74"/><rect x="3" y="4" width="8" height="3" fill="#e8eaee"/></svg>
      <div><b>Fax</b>(555) 014-2291</div>
    </div>
  </div>
</section>

<footer class="section site-footer">
  <div class="socials"><span></span><span></span><span></span></div>
  <nav class="footer-nav"><span>Home</span><span>About Us</span><span>Services</span><span>Gallery</span><span>Contact Us</span></nav>
  <div class="footer-rule"></div>
  <p class="copyright">&copy; 2017 Bramble Fork Builders LLC. All rights reserved.</p>
</footer>

</body>
</html>
```